Lantern Ridge Consulting

I need a business card design and for my consulting business. I provide outsourced CFO services for start-ups and high growth companies. I call my company Lantern Ridge because building a company is similar to building a stone pathway, selecting each stone and planning several stones head in order to properly place them - all while keeping an eye on the final design and curve of the path. The underlying idea I want to express with my marketing images is that I'm someone that you can count on to help build your business and be there step by step to help. I'm not the old gray-haired CFO that many folks think of. :) I've included a one-page summery that I'm working on, it includes a summary of what I do. I've used a muted pathway and with greens in the header , and do like the green, but am open to other colors if they work well. Would like something that looks like a pathway, but a more abstract version instead of a picture.

Marketing

```html
<!DOCTYPE html>
<html lang="en">
<head>
<meta charset="utf-8">
<title>Lantern Ridge Consulting – Business Card</title>
<link rel="stylesheet" href="https://fonts.googleapis.com/css2?family=Ubuntu:wght@400;500;700&display=swap">
<style>
  :root {
    --stage: #2b2b2b;
    --card: #ffffff;
    --band-light: #dcebc6;
    --band-mid: #c9dfac;
    --green: #6ab02e;
    --green-dark: #5a9a24;
    --gray-bar: #6a6a6a;
    --ink: #3c3c3c;
    --ink-soft: #555555;
    --divider: #4a4a4a;
    --tagline: #8a8a8a;
  }
  * { margin: 0; padding: 0; box-sizing: border-box; }
  html, body {
    width: 1200px; height: 900px; overflow: hidden;
    background: var(--stage);
    font-family: "Ubuntu", sans-serif;
  }
  .stage { position: relative; width: 1200px; height: 900px; }

  .card {
    position: absolute; left: 290px;
    width: 620px; height: 354px;
    background: var(--card);
    overflow: hidden;
  }
  .card--back { top: 70px; }
  .card--front { top: 476px; }

  /* back side */
  .back-texture {
    position: absolute; left: 0; top: 0; width: 100%; height: 100%;
    background: radial-gradient(ellipse at 78% 30%, #ececec 0%, #f6f6f6 40%, #ffffff 75%);
  }
  .back-tagline {
    position: absolute; left: 0; right: 0; top: 150px;
    text-align: center; color: var(--tagline);
    font-size: 27px; line-height: 1.25; letter-spacing: 0.5px;
  }
  .back-stripe {
    position: absolute; left: 0; right: 0; bottom: 0; height: 16px;
    background: var(--green);
  }

  /* front side */
  .front-band {
    position: absolute; left: 0; right: 0; top: 48px; height: 168px;
    background: linear-gradient(90deg, var(--band-light) 0%, var(--band-mid) 100%);
  }
  .contact {
    position: absolute; right: 362px; top: 98px;
    text-align: right; color: var(--ink);
  }
  .contact__name { font-size: 17px; font-weight: 700; letter-spacing: 0.6px; }
  .contact__role { font-size: 12px; color: var(--ink-soft); margin-top: 1px; }
  .contact__line { font-size: 13px; color: var(--ink-soft); line-height: 1.35; letter-spacing: 0.3px; }
  .divider {
    position: absolute; left: 284px; top: 80px; width: 2px; height: 106px;
    background: var(--divider);
  }
  .brand {
    position: absolute; left: 330px; top: 72px;
    color: var(--ink); font-size: 34px; font-weight: 400; line-height: 1.05;
  }
  .brand span { display: block; }
  .brand span:nth-child(2) { padding-left: 50px; }

  .accent-bar {
    position: absolute; top: 236px; height: 10px;
  }
  .accent-bar--green { left: 0; width: 75%; background: var(--green); }
  .accent-bar--gray { left: 76.5%; right: 0; background: var(--gray-bar); }
  .front-stripe {
    position: absolute; left: 0; right: 0; bottom: 0; height: 20px;
    background: var(--green-dark);
  }
</style>
</head>
<body>
<main class="stage">
  <section class="card card--back" aria-label="Card back">
    <div class="back-texture" role="img" aria-label="Faint scattered stepping-stone squares suggesting a path"></div>
    <p class="back-tagline">Helping Build Businesses<br>One Step at a time</p>
    <div class="back-stripe"></div>
  </section>

  <section class="card card--front" aria-label="Card front">
    <div class="front-band" role="img" aria-label="Light green band with faint stepping-stone squares"></div>
    <div class="contact">
      <p class="contact__name">Daniel Reed Marsh</p>
      <p class="contact__role">Principal</p>
      <p class="contact__line">+1 555 014 2298</p>
      <p class="contact__line">daniel@lanternridge.com</p>
      <p class="contact__line">www.lanternridge.com</p>
    </div>
    <div class="divider"></div>
    <p class="brand"><span>Lantern</span><span>Ridge</span></p>
    <div class="accent-bar accent-bar--green"></div>
    <div class="accent-bar accent-bar--gray"></div>
    <div class="front-stripe"></div>
  </section>
</main>
</body>
</html>
```